Larkwell Bend responsive web design

We need a responsive, bootstrap compatible (but design only - PSD files) website design for a fly fishing shop and guide service.

Design should be very clean. Home Page design + interior page design please.

Possible Home Page Content:
Slide Show
Highlight Three Features: Guided Trips, Fly Shop, Missouri River
About

Thank you and good luck!

Industry/Entity Type

Shop

Requirements
Must have
• This will be used on Bootstrap CMS so needs 12 column bootstrap measurements.

DESIGN ONLY NEEDED (clean PSD files), no programming required.
Need a Home Page layout and secondary page layout

Must show use of the following:
H1 - H5 font uses
link color
Dropdown for navigation bar
Button example
Should not have
• No cutout images, this will be part of CMS and client needs to be able to update most content without knowing photoshop.

```html
<!DOCTYPE html>
<html lang="en">
<head>
<meta charset="utf-8">
<title>Larkwell Bend – Fly Shop &amp; Guide Service</title>
<link rel="stylesheet" href="https://fonts.googleapis.com/css2?family=Oswald:wght@300;400;500;700&family=Open+Sans:wght@400;600;700&display=swap">
<style>
:root{
  --nav-dark:#1f0b12;
  --sky-blue:#3aa9e0;
  --feature-blue:#4db4e4;
  --brand-red:#c4363c;
  --text-grey:#6b6b6b;
  --text-dark:#333333;
  --footer-brown:#2c2119;
  --footer-base:#161010;
  --white:#ffffff;
  --line-grey:#d9d9d9;
}
*{margin:0;padding:0;box-sizing:border-box}
html,body{width:708px;height:1200px;overflow:hidden}
body{position:relative;background:var(--white);font-family:"Open Sans",Arial,sans-serif;color:var(--text-dark)}
.abs{position:absolute}

/* Header */
.site-header{position:absolute;left:0;top:0;width:708px;height:47px;background:var(--nav-dark);z-index:5}
.brand{position:absolute;left:90px;top:0;width:106px;height:69px;background:var(--nav-dark);border:4px solid #8a8585;border-top:none;display:flex;align-items:center;justify-content:center;z-index:6}
.brand-name{font-family:"Oswald",sans-serif;font-weight:500;font-size:15px;color:#7fd0f2;letter-spacing:.3px}
.main-nav a{position:absolute;top:20px;font-family:"Oswald",sans-serif;font-weight:400;font-size:10.5px;color:var(--white);text-decoration:none;white-space:nowrap}
.main-nav a.active{color:var(--sky-blue)}
.nav-sep{position:absolute;top:20px;font-family:"Oswald",sans-serif;font-size:10.5px;color:var(--white)}
.nav-caret{position:absolute;left:393px;top:41px;width:0;height:0;border-left:6px solid transparent;border-right:6px solid transparent;border-bottom:6px solid var(--sky-blue)}
.dropdown{position:absolute;left:319px;top:49px;width:108px;height:81px;background:#2a1a1c;border:3px solid #6d6566;border-top:2px solid var(--sky-blue);z-index:6}
.dropdown a{display:block;height:20px;line-height:19px;padding-left:11px;font-size:7px;color:#e6e6e6;text-decoration:none;border-bottom:1px solid #514446}
.dropdown a.current{color:var(--sky-blue)}

/* Hero */
.hero{position:absolute;left:0;top:47px;width:708px;height:331px;background:linear-gradient(180deg,#6f7a86 0%,#b8a48a 28%,#c7874a 46%,#8a6a45 56%,#7c8692 70%,#5f6b78 100%)}
.hero-title{position:absolute;left:0;top:160px;width:708px;text-align:center;font-family:"Oswald",sans-serif;font-weight:700;font-size:21px;color:var(--white);letter-spacing:.2px}
.hero-sub{position:absolute;left:90px;top:194px;width:528px;text-align:center;font-family:"Oswald",sans-serif;font-weight:300;font-size:15px;line-height:18px;color:var(--white)}
.slider-dots{position:absolute;left:340px;top:358px;display:flex;gap:3px}
.slider-dots span{width:7px;height:7px;border:1px solid var(--white);border-radius:50%}
.slider-dots span.on{background:var(--white)}

/* Welcome */
.welcome-title{position:absolute;left:0;top:399px;width:708px;text-align:center;font-family:"Oswald",sans-serif;font-weight:300;font-size:22px;color:var(--sky-blue)}
.welcome-text{position:absolute;left:92px;top:436px;width:524px;text-align:center;font-size:8.4px;line-height:13.4px;color:var(--text-grey)}
.btn-red{position:absolute;background:var(--brand-red);color:var(--white);font-family:"Oswald",sans-serif;font-size:11px;text-align:center}
.btn-learn{left:292px;top:489px;width:124px;height:25px;line-height:25px}

/* Features */
.features{position:absolute;left:0;top:541px;width:708px;height:266px;background:linear-gradient(180deg,#58bbe8 0%,#3fa8da 45%,#4cb2e2 60%,#58bbe8 100%)}
.features-title{position:absolute;left:0;top:16px;width:708px;text-align:center;font-family:"Oswald",sans-serif;font-weight:300;font-size:22px;color:var(--white)}
.feature-card{position:absolute;top:65px;width:164px}
.feature-photo{width:164px;height:74px;border:1px solid var(--white);padding:3px}
.feature-photo div{width:100%;height:100%}
.feature-card h3{margin-top:11px;font-family:"Oswald",sans-serif;font-weight:400;font-size:12px;color:var(--white)}
.feature-card p{margin-top:3px;font-size:7.6px;line-height:9.6px;color:var(--white)}
.btn-outline{display:block;margin-top:11px;width:63px;height:21px;line-height:19px;border:1px solid var(--white);font-family:"Oswald",sans-serif;font-size:9px;color:var(--white);text-align:center}
.btn-outline.filled{background:var(--brand-red);border-color:var(--brand-red)}

/* Testimonial & newsletter */
.quote-mark{position:absolute;left:161px;top:826px;font-family:Georgia,serif;font-size:38px;line-height:38px;color:#c8d0d6;font-weight:700}
.section-heading{position:absolute;font-family:"Oswald",sans-serif;font-weight:300;font-size:13px}
.testimonial-photo{position:absolute;left:92px;top:860px;width:75px;height:73px;border:1px solid var(--line-grey);padding:2px;background:var(--white)}
.testimonial-photo div{width:100%;height:100%;background:linear-gradient(180deg,#7a8a6a 0%,#5a6650 55%,#8c7a5a 100%)}
.testimonial-text{position:absolute;left:192px;top:868px;width:210px;font-size:7.6px;line-height:9.8px;color:#8a8a8a}
.testimonial-name{position:absolute;left:192px;top:914px;font-size:7.8px;font-weight:600;color:var(--text-dark)}
.testimonial-date{position:absolute;left:192px;top:925px;font-size:7.6px;color:var(--text-grey)}
.divider{position:absolute;left:422px;top:832px;width:1px;height:101px;background:#e3e3e3}
.email-field{position:absolute;left:450px;top:876px;width:165px;height:24px;border:1px solid #dcdcdc;background:#f5f5f5;font-size:7px;color:#9a9a9a;line-height:22px;padding-left:8px}
.btn-submit{position:absolute;left:450px;top:910px;width:63px;height:21px;line-height:21px;background:var(--sky-blue);color:var(--white);font-family:"Oswald",sans-serif;font-size:9px;text-align:center}

/* Footer */
.site-footer{position:absolute;left:0;top:962px;width:708px;height:203px;background:linear-gradient(135deg,#3a2c20 0%,#2a1f18 50%,#3b2d1f 100%)}
.footer-heading{position:absolute;top:23px;font-family:"Oswald",sans-serif;font-weight:300;font-size:13px;color:var(--sky-blue)}
.view-all{position:absolute;left:231px;top:27px;font-family:"Oswald",sans-serif;font-size:8.5px;color:var(--white);text-decoration:underline}
.thumb{position:absolute;width:54px;height:54px;border:1px solid #d8d8d8;padding:2px}
.thumb div{width:100%;height:100%}
.social-icon{position:absolute;left:284px;width:24px;height:24px}
.social-label{position:absolute;left:316px;font-size:7.8px;font-weight:700;color:var(--white);letter-spacing:.4px}
.contact-intro{position:absolute;left:450px;top:66px;width:170px;font-size:7.6px;line-height:11px;font-weight:600;color:var(--white)}
.contact-line{position:absolute;left:471px;font-size:7.6px;line-height:11px;color:var(--white)}
.contact-icon{position:absolute;left:451px}
.copyright-bar{position:absolute;left:0;top:1165px;width:708px;height:35px;background:var(--footer-base);text-align:center;line-height:35px;font-size:7.8px;color:#9a9a9a}
.copyright-bar strong{color:var(--white);font-weight:600}
</style>
</head>
<body>

<header class="site-header">
  <div class="brand"><span class="brand-name">Larkwell Bend</span></div>
  <nav class="main-nav">
    <a class="active" style="left:269px">Home</a>
    <span class="nav-sep" style="left:302px">/</span>
    <a style="left:316px">About Us</a>
    <span class="nav-sep" style="left:360px">/</span>
    <a class="active" style="left:374px">Guided Trips</a>
    <span class="nav-sep" style="left:429px">/</span>
    <a style="left:443px">Fly Shop</a>
    <span class="nav-sep" style="left:485px">/</span>
    <a style="left:501px">Missouri River</a>
    <span class="nav-sep" style="left:563px">/</span>
    <a style="left:577px">Contact Us</a>
  </nav>
  <div class="nav-caret"></div>
</header>

<div class="dropdown">
  <a class="current">Menu One Detail Here</a>
  <a>Menu Two Detail Here</a>
  <a>Menu Three Detail Here</a>
</div>

<section class="hero" role="img" aria-label="Slideshow photo: river at sunset with golden grass banks and mountains under clouds">
  <h1 class="hero-title">LOREM IPSUM DOLOR SIT AMET, CONSECTETUR ELIT.</h1>
  <p class="hero-sub">Sed dignissim, sem viverra rutrum condimentum, tortor massa tristique mi, sit amet tincidunt dolor lectus sed leo. Etiam interdum erat dui, nec ullamcorper eros hendrerit vitae.</p>
  <div class="slider-dots"><span></span><span class="on"></span><span></span></div>
</section>

<h2 class="welcome-title">WELCOME TO LARKWELL BEND</h2>
<p class="welcome-text">Donec sed nulla nec felis tincidunt consequat sit amet vel felis. Praesent fermentum auctor orci, rhoncus adipiscing lectus convallis rhoncus. Mauris nec dui mauris. Proin adipiscing justo ac mauris facilisis, eu posuere dolor luctus. Integer aliquam ligula vestibu lorem semper, sed adipiscing felis accumsan.</p>
<div class="btn-red btn-learn">Learn More</div>

<section class="features" role="img" aria-label="Background photo: tree-lined river reflection tinted blue">
  <h2 class="features-title">OUR FEATURES</h2>
  <div class="feature-card" style="left:92px">
    <div class="feature-photo"><div role="img" aria-label="Photo: two anglers in a drift boat on the river" style="background:linear-gradient(180deg,#8c8070 0%,#a08a6c 45%,#4f5a58 100%)"></div></div>
    <h3>Guided Trips</h3>
    <p>Sed dignissim, sem viverra rutrum condiment tortor massa tristique mi, sit amet tincidunt dolor lectus sed leo. Etiam interdum erat dui, neculla mcorper eros hendrerit vitae.</p>
    <span class="btn-outline">Read More</span>
  </div>
  <div class="feature-card" style="left:271px">
    <div class="feature-photo"><div role="img" aria-label="Photo: fly shop interior with display tables and shelves" style="background:linear-gradient(180deg,#8a7048 0%,#b08a4c 50%,#6a5236 100%)"></div></div>
    <h3>Fly Shop</h3>
    <p>Sed dignissim, sem viverra rutrum condiment tortor massa tristique mi, sit amet tincidunt dolor lectus sed leo. Etiam interdum erat dui, neculla mcorper eros hendrerit vitae.</p>
    <span class="btn-outline">Read More</span>
  </div>
  <div class="feature-card" style="left:451px">
    <div class="feature-photo"><div role="img" aria-label="Photo: rocky bluff above a calm river" style="background:linear-gradient(180deg,#a9bccb 0%,#7d7a60 45%,#5d5a48 65%,#6c7a86 100%)"></div></div>
    <h3>Missouri River</h3>
    <p>Sed dignissim, sem viverra rutrum condiment tortor massa tristique mi, sit amet tincidunt dolor lectus sed leo. Etiam interdum erat dui, neculla mcorper eros hendrerit vitae.</p>
    <span class="btn-outline filled">Read More</span>
  </div>
</section>

<div class="quote-mark">&ldquo;</div>
<h3 class="section-heading" style="left:191px;top:843px;color:var(--sky-blue)">Client Testimonial</h3>
<div class="testimonial-photo"><div role="img" aria-label="Photo: client holding a large trout"></div></div>
<p class="testimonial-text">Phasellus egestas in est quis consectetur. Nullam scelerisque tincidunt. Morbi nec felis faucibus, porta sapien sit amet, suscipit nisi. Mauris ac tortor id odio auctor vehicula sed venenatis elit.</p>
<p class="testimonial-name">Dane Holloway,</p>
<p class="testimonial-date">Janvery - 08 - 2014</p>
<div class="divider"></div>
<h3 class="section-heading" style="left:450px;top:843px;color:var(--text-dark)">Subscribe to our Newsletter</h3>
<div class="email-field">Your E-mail</div>
<div class="btn-submit">Submit Now</div>

<footer class="site-footer" role="img" aria-label="Background photo: dimly lit fly shop interior">
  <h4 class="footer-heading" style="left:92px">OUR GALLERY</h4>
  <span class="view-all">View All</span>
  <div class="thumb" style="left:92px;top:62px"><div role="img" aria-label="Photo: shop building" style="background:linear-gradient(180deg,#9db4c8,#8a7a60)"></div></div>
  <div class="thumb" style="left:148px;top:62px"><div role="img" aria-label="Photo: shop interior" style="background:linear-gradient(180deg,#8a6a40,#a8843e)"></div></div>
  <div class="thumb" style="left:205px;top:62px"><div role="img" aria-label="Photo: shop interior" style="background:linear-gradient(180deg,#8a6a40,#a8843e)"></div></div>
  <div class="thumb" style="left:92px;top:119px"><div role="img" aria-label="Photo: anglers on the river" style="background:linear-gradient(180deg,#8c8070,#4f5a58)"></div></div>
  <div class="thumb" style="left:148px;top:119px"><div role="img" aria-label="Photo: river bluff" style="background:linear-gradient(180deg,#a9bccb,#6c6a54)"></div></div>
  <div class="thumb" style="left:205px;top:119px"><div role="img" aria-label="Photo: river bluff" style="background:linear-gradient(180deg,#a9bccb,#6c6a54)"></div></div>

  <h4 class="footer-heading" style="left:283px">CONNECT WITH US</h4>
  <span class="social-icon" style="top:62px;background:#3b5b98"></span>
  <span class="social-label" style="top:70px">CHATTERLY</span>
  <span class="social-icon" style="top:91px;background:#45b0e3"></span>
  <span class="social-label" style="top:99px">CHIRPLINE</span>
  <span class="social-icon" style="top:118px;background:#f08a24"></span>
  <span class="social-label" style="top:126px">BLOG</span>
  <span class="social-icon" style="top:147px;background:#1a8fd0"></span>
  <span class="social-label" style="top:155px">WORKNET</span>

  <h4 class="footer-heading" style="left:450px">CONTECT US</h4>
  <p class="contact-intro">Lorem ipsum dolor sit amet, consectetur elit. Suspendisse quis tincidunt odio. Nullam nec semper nisi orci suscipit gravida.</p>
  <svg class="contact-icon" style="top:113px" width="13" height="12" viewBox="0 0 13 12"><path d="M6.5 0 13 6h-2v6H8V8H5v4H2V6H0z" fill="#fff"/></svg>
  <p class="contact-line" style="top:111px">18 Willow Ferry Road<br>Cascade Flats, MT 59000</p>
  <svg class="contact-icon" style="top:147px" width="13" height="9" viewBox="0 0 13 9"><path d="M1 3C3-.5 10-.5 12 3l-2.5 1L8 2.5H5L3.5 4z M3 5h7l1 4H2z" fill="#fff"/></svg>
  <p class="contact-line" style="top:145px">(406) 555-0142</p>
  <svg class="contact-icon" style="top:169px" width="13" height="9" viewBox="0 0 13 9"><rect x=".5" y=".5" width="12" height="8" fill="none" stroke="#fff"/><path d="M.5.5 6.5 5l6-4.5" fill="none" stroke="#fff"/></svg>
  <p class="contact-line" style="top:166px">info@larkwellbend.com</p>
</footer>

<div class="copyright-bar">Copyright © 2014 <strong>Larkwell Bend.</strong></div>

</body>
</html>
```